business card for a massage therapy practice named 'Meadow and Willow Massage Studio'

I really need a trendy, yet easy on the eyes business card to complement my logo. Ideally with some gold or rose gold foil work.

My uploaded file of the logo I have in horizontal but I have a vertical version as well. Another color that is used in the website is a blush pink here and there. I'd like to see some trendy tropical leaves in the design.

```html
<!DOCTYPE html>
<html lang="en">
<head>
<meta charset="utf-8">
<title>Meadow and Willow Massage Studio – Business Card</title>
<link href="https://fonts.googleapis.com/css2?family=Montserrat:wght@600&family=Questrial&display=swap" rel="stylesheet">
<style>
  :root {
    --backdrop: #151515;
    --card-white: #f6f5f3;
    --blush: #e8868f;
    --blush-light: #eb939a;
    --ink: #2a2a2a;
    --rose-text: #e2727d;
    --gold: #b49a6a;
    --leaf-dark: #2f8a2f;
    --leaf-mid: #4fae3c;
    --leaf-light: #8fd06a;
    --mint: #7fd3c4;
  }
  * { box-sizing: border-box; margin: 0; padding: 0; }
  html, body { width: 1200px; height: 982px; overflow: hidden; }
  body {
    background: var(--backdrop);
    font-family: "Questrial", "Helvetica Neue", sans-serif;
    position: relative;
  }
  .card {
    position: absolute;
    top: 170px;
    width: 370px;
    height: 640px;
    overflow: hidden;
    box-shadow: 0 18px 40px rgba(0,0,0,.55);
  }
  .card--front { left: 190px; background: var(--card-white); }
  .card--back { left: 640px; background: var(--blush); }

  .foliage {
    position: absolute;
    border-radius: 50%;
    background: radial-gradient(ellipse at center, var(--leaf-light) 0%, var(--leaf-mid) 50%, var(--leaf-dark) 100%);
  }
  .foliage--top-left { top: -80px; left: -90px; width: 240px; height: 180px; }
  .foliage--bottom-left { bottom: -70px; left: 30px; width: 190px; height: 140px; }
  .foliage--bottom-right { bottom: -60px; right: -70px; width: 200px; height: 170px; }

  .brand {
    position: absolute;
    left: 0; right: 0;
    text-align: center;
    color: var(--ink);
  }
  .brand__dot {
    display: block;
    width: 34px; height: 34px;
    margin: 0 auto 18px;
    border-radius: 50%;
    background: linear-gradient(135deg, #d8c293, var(--gold) 55%, #8e7449);
  }
  .brand__name { font-size: 30px; line-height: 1.15; letter-spacing: .5px; }
  .brand__sub { font-size: 17px; letter-spacing: 4px; text-transform: uppercase; margin-top: 8px; color: var(--mint); }
  .card--front .brand { top: 160px; }

  .contact { position: absolute; left: 46px; top: 372px; }
  .contact__name {
    font-family: "Montserrat", "Helvetica Neue", sans-serif;
    font-weight: 600; font-size: 26px; color: var(--rose-text);
  }
  .contact__role { font-size: 14px; color: var(--ink); margin-top: 2px; }
  .contact__list { list-style: none; margin-top: 18px; }
  .contact__item {
    display: flex; align-items: center; gap: 12px;
    font-size: 14px; color: var(--ink); margin-bottom: 8px;
  }
  .contact__item svg { width: 14px; height: 14px; fill: var(--gold); flex: none; }

  .foliage--band-top { top: -60px; left: -40px; width: 450px; height: 200px; }
  .foliage--band-bottom { bottom: -60px; left: -40px; width: 450px; height: 210px; }
  .back__disc {
    position: absolute;
    left: 20px; top: 95px;
    width: 330px; height: 450px;
    border-radius: 50%;
    background: var(--blush-light);
  }
  .card--back .brand { top: 200px; }
  .back__url { font-size: 14px; color: #fff; margin-top: 26px; letter-spacing: .5px; }
</style>
</head>
<body>

  <section class="card card--front" aria-label="Business card front">
    <div class="foliage foliage--top-left" role="img" aria-label="Tropical palm leaves in the corner"></div>
    <div class="foliage foliage--bottom-left" role="img" aria-label="Broad tropical leaves"></div>
    <div class="foliage foliage--bottom-right" role="img" aria-label="Tropical palm leaves in the corner"></div>

    <div class="brand">
      <span class="brand__dot"></span>
      <p class="brand__name">Meadow and Willow</p>
      <p class="brand__sub">Massage Studio</p>
    </div>

    <div class="contact">
      <p class="contact__name">Nora Bell</p>
      <p class="contact__role">Founder &amp; CEO</p>
      <ul class="contact__list">
        <li class="contact__item">
          <svg viewBox="0 0 24 24"><path d="M6.6 10.8a15.1 15.1 0 0 0 6.6 6.6l2.2-2.2c.3-.3.7-.4 1-.2 1.1.4 2.3.6 3.6.6.6 0 1 .4 1 1V20c0 .6-.4 1-1 1A17 17 0 0 1 3 4c0-.6.4-1 1-1h3.5c.6 0 1 .4 1 1 0 1.3.2 2.5.6 3.6.1.3 0 .7-.2 1z"/></svg>
          <span>555 014 268</span>
        </li>
        <li class="contact__item">
          <svg viewBox="0 0 24 24"><path d="M2 5h20v14H2zm2 2v.5l8 5 8-5V7zm0 3v7h16v-7l-8 5z"/></svg>
          <span>nora@meadow-willow.com</span>
        </li>
        <li class="contact__item">
          <svg viewBox="0 0 24 24"><path d="M12 2a10 10 0 1 0 0 20 10 10 0 0 0 0-20zm6.9 9h-3a15 15 0 0 0-1.3-6A8 8 0 0 1 18.9 11zM12 4c.9 1.2 1.8 3.8 1.9 7h-3.8c.1-3.2 1-5.8 1.9-7zM9.4 5a15 15 0 0 0-1.3 6h-3A8 8 0 0 1 9.4 5zM5.1 13h3a15 15 0 0 0 1.3 6A8 8 0 0 1 5.1 13zM12 20c-.9-1.2-1.8-3.8-1.9-7h3.8c-.1 3.2-1 5.8-1.9 7zm2.6-1a15 15 0 0 0 1.3-6h3a8 8 0 0 1-4.3 6z"/></svg>
          <span>www.meadow-willow.com</span>
        </li>
      </ul>
    </div>
  </section>

  <section class="card card--back" aria-label="Business card back">
    <div class="foliage foliage--band-top" role="img" aria-label="Tropical leaves framing the top of the oval"></div>
    <div class="foliage foliage--band-bottom" role="img" aria-label="Tropical leaves framing the bottom of the oval"></div>
    <div class="back__disc"></div>

    <div class="brand">
      <span class="brand__dot"></span>
      <p class="brand__name">Meadow and Willow</p>
      <p class="brand__sub">Massage Studio</p>
      <p class="back__url">www.meadow-willow.com</p>
    </div>
  </section>

</body>
</html>
```